Flyer-Design für Fellglück Service
Zielgruppe
Fellglück Service bietet Haustierbetreuung in Nürnberg und Fürth an. Betreut werden Hunde, Katzen und Kleintiere. Die Zielgruppe ist also 18+ Jahre mit einen Haustier, dass betreut werden soll. Die Hauptzielgruppe sind Hundebesitzer die Tagesbetreuung oder Gassi-Service suchen.
Aufgabenstellung
Formate bitte alle üblichen Flyer Größen. Wer Fleißig ist macht auch Vorschläge für eine Broschüre. Wer eine gute Idee hat für einen Gutschein, kann diesen mit einbauen. Der angehängte Flyer wurde von mir selbst gestaltet, also bitte nich wundern, ob der unprofessionalität.
Mehr Input findet Ihr auf www.fellglueck-service.de oder auf der Freundesbuch Seite Fellglück Service.
Den Flyer bitte beidseitig konziieren.

```html
<!DOCTYPE html>
<html lang="de">
<head>
<meta charset="utf-8">
<title>Fellglück Service – Flyer</title>
<link href="https://fonts.googleapis.com/css2?family=Open+Sans:ital,wght@0,400;0,700;0,800;1,700&family=Comic+Neue:wght@700&display=swap" rel="stylesheet">
<style>
  :root{
    --stage:#c9d0d8;
    --yellow:#d8c021;
    --yellow-text:#d2b40e;
    --green:#4ca93b;
    --green-text:#3d9a35;
    --white:#ffffff;
    --photo-fur:#c99a5e;
    --photo-dark:#3b3a3a;
    --photo-cat:#9c8467;
    --photo-hamster:#e8d2b8;
    --photo-grass:#b9c8a0;
  }
  *{box-sizing:border-box;margin:0;padding:0}
  html,body{width:1200px;height:797px;overflow:hidden}
  body{background:var(--stage);font-family:"Open Sans",sans-serif;position:relative}
  .flyer{position:absolute;left:330px;top:22px;width:540px;height:752px;overflow:hidden;box-shadow:0 6px 24px rgba(0,0,0,.18)}
  .flyer-inner{position:absolute;left:0;top:0;width:880px;height:1225px;transform:scale(.6136);transform-origin:0 0;background:var(--white)}
  .artwork{position:absolute;inset:0;width:880px;height:1225px}
  .tagline-text{font-family:"Comic Neue",sans-serif;font-weight:700;font-size:19px;fill:var(--yellow-text)}
  .brand-name{position:absolute;left:520px;top:88px;width:320px;text-align:center;font-weight:700;font-size:34px;color:var(--green-text)}
  .social-row{position:absolute;left:475px;top:665px;display:flex;gap:14px}
  .social-item{display:flex;flex-direction:column;align-items:center;width:70px;gap:4px}
  .social-item .square{width:48px;height:48px}
  .social-item span{font-size:11px;font-weight:700;color:var(--green-text)}
  .sq-yellow{background:var(--yellow)}
  .sq-green{background:var(--green)}
  .info-heading{position:absolute;left:476px;top:730px;font-weight:800;font-size:24px;color:var(--yellow-text);letter-spacing:.5px}
  .info-body{position:absolute;left:476px;top:790px;font-size:18px;line-height:22.5px;color:var(--green-text)}
  .intro-heading{position:absolute;left:74px;top:728px;font-weight:800;font-size:24px;line-height:30px;color:var(--white);text-transform:uppercase;letter-spacing:.3px}
  .intro-body{position:absolute;left:74px;top:866px;font-size:18px;line-height:22.5px;color:var(--white)}
  .voucher{position:absolute;left:0;top:1010px;width:896px;text-align:center;color:var(--white)}
  .voucher h2{font-weight:800;font-size:38px;color:var(--yellow);letter-spacing:1px}
  .voucher p{font-size:29px;font-weight:400;line-height:36px;margin-top:22px}
  .voucher em{font-weight:700;color:var(--yellow)}
  .voucher small{display:block;font-size:16px;margin-top:10px}
</style>
</head>
<body>
<div class="flyer">
  <div class="flyer-inner">
    <svg class="artwork" viewBox="0 0 880 1225" xmlns="http://www.w3.org/2000/svg">
      <defs>
        <radialGradient id="fur" cx=".5" cy=".5" r=".6"><stop offset="0" stop-color="#d8ae74"/><stop offset="1" stop-color="#b48348"/></radialGradient>
        <radialGradient id="cat" cx=".5" cy=".5" r=".6"><stop offset="0" stop-color="#a89277"/><stop offset="1" stop-color="#d99a2e"/></radialGradient>
        <radialGradient id="blackdog" cx=".5" cy=".5" r=".6"><stop offset="0" stop-color="#2e2e30"/><stop offset="1" stop-color="#6f655c"/></radialGradient>
        <radialGradient id="hamster" cx=".4" cy=".4" r=".7"><stop offset="0" stop-color="#e3b48a"/><stop offset="1" stop-color="#eceae6"/></radialGradient>
        <linearGradient id="grass" x1="0" y1="0" x2="0" y2="1"><stop offset="0" stop-color="#8fa86a"/><stop offset=".5" stop-color="#efe6d8"/><stop offset="1" stop-color="#7f9a56"/></linearGradient>
        <path id="tagline-arc" d="M510 95 Q680 20 855 95"/>
      </defs>
      <rect class="column-yellow" x="0" y="0" width="449" height="980" fill="var(--yellow)"/>
      <rect class="band-green" x="0" y="977" width="880" height="248" fill="var(--green)"/>
      <line x1="0" y1="977" x2="880" y2="977" stroke="#ffffff" stroke-width="3" stroke-dasharray="2 6" opacity=".6"/>

      <g role="img" aria-label="Foto: Nahaufnahme eines älteren Golden Retrievers">
        <ellipse cx="290" cy="150" rx="205" ry="175" transform="rotate(-30 290 150)" fill="url(#fur)" stroke="#fff" stroke-width="10"/>
      </g>
      <g role="img" aria-label="Foto: schlafende getigerte Katze">
        <ellipse cx="120" cy="500" rx="165" ry="215" transform="rotate(-25 120 500)" fill="url(#cat)" stroke="#fff" stroke-width="10"/>
      </g>
      <g role="img" aria-label="Foto: schwarzer Labrador auf Waldboden">
        <ellipse cx="443" cy="475" rx="145" ry="168" transform="rotate(-20 443 475)" fill="none" stroke="var(--yellow)" stroke-width="5" stroke-dasharray="1 9" stroke-linecap="round"/>
        <ellipse cx="443" cy="472" rx="132" ry="155" transform="rotate(-20 443 472)" fill="url(#blackdog)" stroke="#fff" stroke-width="6"/>
      </g>
      <g role="img" aria-label="Foto: Hamster auf einer Hand">
        <ellipse cx="760" cy="455" rx="165" ry="192" transform="rotate(-25 760 455)" fill="none" stroke="var(--yellow)" stroke-width="5" stroke-dasharray="1 9" stroke-linecap="round"/>
        <ellipse cx="760" cy="452" rx="152" ry="180" transform="rotate(-25 760 452)" fill="url(#hamster)" stroke="#fff" stroke-width="6"/>
      </g>
      <g role="img" aria-label="Foto: Hundepfote in einer Hand auf Gras">
        <ellipse cx="790" cy="980" rx="120" ry="105" transform="rotate(-20 790 980)" fill="#fff" stroke="var(--green)" stroke-width="5" stroke-dasharray="1 9" stroke-linecap="round"/>
        <ellipse cx="790" cy="980" rx="108" ry="93" transform="rotate(-20 790 980)" fill="url(#grass)"/>
      </g>

      <text class="tagline-text"><textPath href="#tagline-arc" startOffset="50%" text-anchor="middle">Eine liebevolle Betreuung für Ihr Haustier!</textPath></text>
      <rect role="img" aria-label="Dekoration: Spur aus Pfotenabdrücken und Fußspuren" x="525" y="158" width="310" height="85" rx="40" fill="var(--green)" opacity=".18"/>
    </svg>

    <div class="brand-name">Fellglück Service</div>

    <div class="social-row">
      <div class="social-item"><div class="square sq-yellow"></div><span>Freundesbuch</span></div>
      <div class="social-item"><div class="square sq-green"></div><span>Kreisnetz</span></div>
      <div class="social-item"><div class="square sq-yellow"></div><span>Zwitscher</span></div>
      <div class="social-item"><div class="square sq-green"></div><span>Plauderpost</span></div>
    </div>

    <h3 class="info-heading">FELLGLÜCK SERVICE</h3>
    <p class="info-body">Bei uns steht Ihr Haustier im Vordergrund.<br>Ob eine einmalige Betreuung, Urlaubs-<br>betreuung oder eine dauerhafte<br>Fürsorge für Ihr Haustier,<br>bei Fellglück Service<br>sind Sie an der<br>richtigen Adresse.</p>

    <h1 class="intro-heading">Sie benötigen eine<br>erfahrene und profes-<br>sionelle Betreuung<br>für Ihr Haustier?</h1>
    <p class="intro-body">Dann bin ich für Sie da!<br>Nutzen Sie gleich eine der vielen<br>Kontaktmöglichkeiten und reservie-<br>ren Sie Ihre Betreuung bei mir.</p>

    <div class="voucher">
      <h2>GUTSCHEIN</h2>
      <p>Bei Vorlage erhalten Sie für Ihre Betreuung<br>einen <em>gratis</em> Kennenlern-Termin mit Ihrem Haustier!*</p>
      <small>*nur gültig, falls eine Betreuung für mich möglich und relevant ist.</small>
    </div>
  </div>
</div>
</body>
</html>
```